Heron Accord Business Card

Need a business card for my nonprofit, Heron Accord Inc. Heron Accord is a conflict resolution practice that offers services that help people resolve problems peacefully.

Got Conflict? Try Conflict Coaching. Initial consultation is complimentary

Marisol Daventry-Kuhl, PhD
Heron Accord Inc.
www.heronaccord-example.org
E: info@heronaccord-example.org
P: 555-318-4927

Would like the attached logo on it, as well as our slogan, which is Finding Calm Around the RoomĀ®

```html
<!DOCTYPE html>
<html lang="en">
<head>
<meta charset="utf-8">
<title>Heron Accord Business Card</title>
<link rel="stylesheet" href="https://fonts.googleapis.com/css2?family=Montserrat:wght@500;600&family=Questrial&display=swap">
<style>
  :root {
    --backdrop: #161616;
    --card: #2a2a2b;
    --card-edge: #232324;
    --gold: #c9a443;
    --gold-soft: #b08d3a;
    --red: #e0262b;
    --ink: #e8e6e2;
  }
  * { box-sizing: border-box; margin: 0; padding: 0; }
  html, body {
    width: 1200px; height: 982px; overflow: hidden;
    background: var(--backdrop);
  }
  .canvas {
    position: relative; width: 1200px; height: 982px;
    display: flex; justify-content: center; align-items: center; gap: 80px;
  }
  .card {
    position: relative; width: 380px; height: 665px;
    background: linear-gradient(160deg, #303031 0%, var(--card) 45%, var(--card-edge) 100%);
    box-shadow: 0 18px 40px rgba(0,0,0,.55);
  }
  .brand {
    position: absolute; left: 0; right: 0; top: 120px;
    display: flex; justify-content: center; align-items: center; gap: 12px;
  }
  .brand-dot {
    width: 14px; height: 14px; border-radius: 50%; background: var(--gold);
  }
  .brand-name {
    font-family: "Montserrat", sans-serif; font-weight: 500;
    font-size: 38px; letter-spacing: 1px; color: var(--gold);
  }
  .person {
    position: absolute; left: 40px; right: 34px; bottom: 150px;
  }
  .person-name {
    font-family: "Montserrat", sans-serif; font-weight: 600;
    font-size: 23px; color: var(--gold); white-space: nowrap;
  }
  .person-rule {
    height: 1.5px; background: var(--red); margin: 6px 0 0 60px;
  }
  .person-title {
    font-family: "Questrial", sans-serif; font-size: 14px;
    color: var(--ink); margin-top: -4px; margin-left: 28px;
  }
  .contacts {
    position: absolute; left: 40px; bottom: 60px;
    list-style: none;
    font-family: "Questrial", sans-serif; font-size: 15px; color: var(--ink);
  }
  .contacts li { display: flex; align-items: center; gap: 12px; line-height: 26px; }
  .contacts svg { width: 13px; height: 13px; flex: none; }
  .slogan {
    position: absolute; left: 0; right: 0; bottom: 120px; text-align: center;
    font-family: "Questrial", sans-serif; font-size: 17px; letter-spacing: .5px;
    color: var(--gold-soft);
  }
</style>
</head>
<body>
<main class="canvas">
  <section class="card card-front" aria-label="Card front">
    <div class="brand">
      <span class="brand-dot"></span>
      <span class="brand-name">Heron Accord</span>
    </div>
    <div class="person">
      <p class="person-name">Marisol Daventry-Kuhl</p>
      <div class="person-rule"></div>
      <p class="person-title">PhD</p>
    </div>
    <ul class="contacts">
      <li>
        <svg viewBox="0 0 16 16" aria-hidden="true"><path fill="#e0262b" d="M3 1l3 3-1.5 2a9 9 0 0 0 5.5 5.5L12 10l3 3-2 2C7 15 1 9 1 3z"/></svg>
        555-318-4927
      </li>
      <li>
        <svg viewBox="0 0 16 16" aria-hidden="true"><rect x="1" y="3" width="14" height="10" fill="#e0262b"/><path d="M1 3l7 6 7-6" fill="none" stroke="#2a2a2b" stroke-width="1.4"/></svg>
        info@heronaccord-example.org
      </li>
      <li>
        <svg viewBox="0 0 16 16" aria-hidden="true"><circle cx="8" cy="8" r="7" fill="#e0262b"/><g fill="none" stroke="#2a2a2b" stroke-width="1"><ellipse cx="8" cy="8" rx="3" ry="7"/><path d="M1 8h14M2.5 4.5h11M2.5 11.5h11"/></g></svg>
        www.heronaccord-example.org
      </li>
    </ul>
  </section>

  <section class="card card-back" aria-label="Card back">
    <div class="brand">
      <span class="brand-dot"></span>
      <span class="brand-name">Heron Accord</span>
    </div>
    <p class="slogan">Finding Calm Around the Room®</p>
  </section>
</main>
</body>
</html>
```